Waste Oil Filter collection & disposal

Basically I need a 1 page website for the business called Grennick Waste Partners.
We are a environmental service provider and we collect and dispose of waste oil filters to protect the environment from hazardous waste oil products.

This is the link to our current website: www.grennickwaste.co.nz

we want it to look fresh and better than our current website. we may potentially look at getting a new logo designed and are open to ideas/designs if you have any.

Industry/Entity Type

Business

Logo Text

Grennick Waste Partners

Number of Pages Required

1 page

Requirements
Must have
• same colours as current website.
• description of what service we provide please refer to leaflet attached

```html
<!DOCTYPE html>
<html lang="en">
<head>
<meta charset="utf-8">
<title>About Us – Grennick Waste Partners</title>
<link href="https://fonts.googleapis.com/css2?family=Open+Sans:wght@300;700&display=swap" rel="stylesheet">
<style>
  :root {
    --page-bg: #ededed;
    --heading: #231f20;
    --body-text: #2b2b2b;
    --green-deep: #1f7a4a;
    --green-mid: #2f9a5f;
    --green-light: #6fb87f;
    --grey-road: #6b6f68;
    --grey-dark: #3f4a4a;
  }
  html, body {
    margin: 0;
    padding: 0;
    overflow: hidden;
    background: #ffffff;
  }
  .about-panel {
    position: relative;
    width: 1200px;
    height: 1037px;
    background: var(--page-bg);
    overflow: hidden;
  }
  .about-panel__art {
    position: absolute;
    inset: 0;
    width: 1200px;
    height: 1037px;
  }
  .about-panel__content {
    position: absolute;
    left: 225px;
    top: 425px;
  }
  .about-panel__label {
    margin: 0 0 36px;
    font-family: "Open Sans", sans-serif;
    font-weight: 700;
    font-size: 42px;
    line-height: 1;
    color: var(--heading);
    letter-spacing: 0.2px;
  }
  .about-panel__intro {
    margin: 0;
    font-family: "Open Sans", sans-serif;
    font-weight: 300;
    font-size: 57px;
    line-height: 69px;
    color: var(--body-text);
  }
</style>
</head>
<body>
<section class="about-panel">
  <svg class="about-panel__art" viewBox="0 0 1200 1037" xmlns="http://www.w3.org/2000/svg">
    <defs>
      <linearGradient id="truck-photo-tone" x1="0" y1="0" x2="1" y2="1">
        <stop offset="0" stop-color="#4f8a55"/>
        <stop offset="0.35" stop-color="#2f8c5c"/>
        <stop offset="0.6" stop-color="#5f6a63"/>
        <stop offset="1" stop-color="#3d8f5a"/>
      </linearGradient>
      <linearGradient id="workshop-tone" x1="0" y1="0" x2="1" y2="1">
        <stop offset="0" stop-color="#4a5a5e"/>
        <stop offset="1" stop-color="#2f3f44"/>
      </linearGradient>
      <linearGradient id="filters-tone" x1="0" y1="0" x2="1" y2="1">
        <stop offset="0" stop-color="#7d8a84"/>
        <stop offset="1" stop-color="#3c4a46"/>
      </linearGradient>
      <linearGradient id="baler-tone" x1="0" y1="0" x2="1" y2="1">
        <stop offset="0" stop-color="#3fa36a"/>
        <stop offset="1" stop-color="#1f7a4a"/>
      </linearGradient>
      <clipPath id="bottom-band">
        <polygon points="161,1037 1200,688 1200,1037"/>
      </clipPath>
    </defs>

    <polygon class="about-panel__hero-photo" role="img"
             aria-label="Photo of a green collection truck parked on gravel beside grass"
             points="0,0 1200,0 1200,42 0,435"
             fill="url(#truck-photo-tone)"/>

    <g clip-path="url(#bottom-band)">
      <rect role="img" aria-label="Photo of grass" x="0" y="680" width="309" height="360" fill="var(--green-light)"/>
      <rect role="img" aria-label="Photo of a workshop interior" x="309" y="680" width="374" height="360" fill="url(#workshop-tone)"/>
      <rect role="img" aria-label="Photo of crushed used oil filters" x="683" y="680" width="253" height="360" fill="url(#filters-tone)"/>
      <rect role="img" aria-label="Photo of a green filter compacting machine" x="936" y="680" width="264" height="360" fill="url(#baler-tone)"/>
    </g>
  </svg>

  <div class="about-panel__content">
    <h2 class="about-panel__label">ABOUT US</h2>
    <p class="about-panel__intro">Grennick Waste Partners Ltd<br>service the Lower North</p>
  </div>
</section>
</body>
</html>
```